Conservative, Modern and Sharp Builder Business card

Hi there,
We would like to update our existing business card.
I have attached photos of existing business card, logo and van sign.

I would like the business card to also list what we do :
Renovation • New Build • Alteration
Extension • Bathroom • Maintenance.(Seperated by dots)

Contact number : 021 0483 0752
(With that exact spacing)

Ideally when people looking from about 2-3 metres, they know that it is a builder’s business card

Open to suggestions on fonts, layout, style of business card

PLEASE ONLY SUBMIT YOUR BEST OR MAX 3 DESIGNS FOR EACH DESIGNER

Thanks

Construction. Renovation

Details should be the same as the existing card. And addition of what we do.

• The new business card must not have the same layout as our existing one. Thanks

```html
<!DOCTYPE html>
<html lang="en">
<head>
<meta charset="utf-8">
<title>KeelCraft Business Card</title>
<link href="https://fonts.googleapis.com/css2?family=Montserrat:wght@700;800&family=Arimo:wght@400;700&display=swap" rel="stylesheet">
<style>
  :root {
    --stage: #e9e9ea;
    --paper: #f4f4f4;
    --paper-shade: #e2e2e2;
    --ink: #1f1f1f;
    --ink-soft: #8a8a8a;
    --ink-muted: #9b9b9b;
    --night: #262626;
    --night-deep: #141414;
    --night-tone: #3a3a3a;
    --white: #ffffff;
  }
  * { box-sizing: border-box; margin: 0; padding: 0; }
  html, body { width: 1200px; height: 801px; overflow: hidden; }
  body {
    background: var(--stage);
    display: flex;
    align-items: center;
    justify-content: center;
    gap: 40px;
  }
  .card {
    position: relative;
    width: 540px;
    height: 309px;
    border-radius: 4px;
    overflow: hidden;
    box-shadow: 0 10px 24px rgba(0,0,0,.12);
  }

  /* Front */
  .card--front { background: linear-gradient(135deg, var(--white), var(--paper) 60%, var(--paper-shade)); }
  .front__decor {
    position: absolute;
    right: 0; top: 0;
    width: 52%; height: 100%;
    background: radial-gradient(ellipse at 55% 55%, #dcdcdc 0%, #e8e8e8 45%, rgba(240,240,240,0) 75%);
  }
  .front__person {
    position: absolute;
    right: 34px; top: 34px;
    text-align: right;
  }
  .person__name {
    font-family: "Arimo", Arial, sans-serif;
    font-weight: 700;
    font-size: 19px;
    letter-spacing: .5px;
    color: var(--ink);
  }
  .person__role {
    font-family: "Arimo", Arial, sans-serif;
    font-size: 14px;
    color: var(--ink-muted);
    margin-top: 3px;
  }
  .front__brand {
    position: absolute;
    left: 34px; top: 92px;
    display: flex;
    align-items: center;
    gap: 10px;
  }
  .brand__mark {
    width: 14px; height: 14px;
    background: var(--ink);
  }
  .brand__name {
    font-family: "Montserrat", sans-serif;
    font-weight: 800;
    font-size: 34px;
    color: var(--ink);
    letter-spacing: -.3px;
  }
  .front__contacts {
    position: absolute;
    left: 36px; bottom: 30px;
    list-style: none;
    font-family: "Arimo", Arial, sans-serif;
    font-size: 14px;
    color: var(--ink-soft);
  }
  .contact {
    display: flex;
    align-items: center;
    gap: 10px;
    line-height: 24px;
  }
  .contact svg { width: 13px; height: 13px; flex: none; }
  .contact__dot {
    width: 11px; height: 11px; margin: 0 1px;
    border-radius: 50%;
    background: var(--ink);
    flex: none;
  }

  /* Back */
  .card--back { background: var(--night); }
  .back__pattern {
    position: absolute; inset: 0;
    background: linear-gradient(120deg, var(--night-deep) 0%, var(--night) 45%, var(--night-tone) 100%);
  }
  .back__content {
    position: absolute; inset: 0;
    display: flex;
    flex-direction: column;
    align-items: center;
    justify-content: center;
    gap: 18px;
    color: var(--white);
  }
  .back__brand {
    display: flex;
    align-items: center;
    gap: 12px;
  }
  .back__brand .brand__mark { background: var(--white); width: 16px; height: 16px; }
  .back__brand .brand__name { color: var(--white); font-size: 44px; }
  .services {
    font-family: "Arimo", Arial, sans-serif;
    font-size: 16px;
    line-height: 1.45;
    text-align: center;
    letter-spacing: .2px;
  }
</style>
</head>
<body>

  <section class="card card--front">
    <div class="front__decor" role="img" aria-label="Large faint brand monogram watermark"></div>

    <div class="front__person">
      <p class="person__name">DAREN HOLLOWAY</p>
      <p class="person__role">Residential Builder</p>
    </div>

    <div class="front__brand">
      <span class="brand__mark"></span>
      <span class="brand__name">KeelCraft</span>
    </div>

    <ul class="front__contacts">
      <li class="contact">
        <svg viewBox="0 0 16 16"><path d="M4 1.5l2.5 3-1.6 1.6a9 9 0 0 0 5 5l1.6-1.6 3 2.5-1.7 2.3C7.5 14 2 8.5 1.7 3.2z" fill="var(--ink)"/></svg>
        <span>021 0483 0752</span>
      </li>
      <li class="contact">
        <svg viewBox="0 0 16 16"><rect x="1" y="3" width="14" height="10" fill="none" stroke="var(--ink)" stroke-width="1.6"/><path d="M1 3.5l7 5.5 7-5.5" fill="none" stroke="var(--ink)" stroke-width="1.6"/></svg>
        <span>KeelCraft@mailbox.co.nz</span>
      </li>
      <li class="contact">
        <svg viewBox="0 0 16 16"><circle cx="8" cy="8" r="6.6" fill="none" stroke="var(--ink)" stroke-width="1.5"/><ellipse cx="8" cy="8" rx="3" ry="6.6" fill="none" stroke="var(--ink)" stroke-width="1.2"/><path d="M1.5 8h13" stroke="var(--ink)" stroke-width="1.2"/></svg>
        <span>www.KeelCraft.nz</span>
      </li>
      <li class="contact">
        <span class="contact__dot"></span>
        <span>KeelCraft.nz</span>
      </li>
    </ul>
  </section>

  <section class="card card--back">
    <div class="back__pattern" role="img" aria-label="Repeating embossed brand monogram pattern in dark greys"></div>
    <div class="back__content">
      <div class="back__brand">
        <span class="brand__mark"></span>
        <span class="brand__name">KeelCraft</span>
      </div>
      <p class="services">
        • Renovation • New Build • Alteration<br>
        • Extension • Bathroom • Maintenance
      </p>
    </div>
  </section>

</body>
</html>
```